Frameless shower doors web site

Build a web site for information and display past projects. Contact information, type of work done. Customer Reviews. The design purpose is to generate phone calls and email inquirers. Domain name is Southernshowerdoors.comEmail is Brightvalebaths@mailbox-demo.com Profile We Love What We Do!Brightvale Bath Panels & Glass LLC. is committed to excellence in every aspect of our business. We hold a standard of integrity bound by fairness, honesty, and personal responsibility. Our distinction is the quality of service and attention to detail we bring to each project. Above all, we listen to our clients input to provide several design options available from designer glass to hardware. We also service and repair existing shower and tub enclosure. Installation of customer purchased enclosure are available by appointment. and address any concerns.

Target Market(s)

25 to 55 residential customers

Number of Pages Required

4 page

Font styles to use
Sans Serif

Colors

Designer to choose colors to be used in the design.

Requirements
Nice to have
• Looking to drive phone calls for estimating shower projects
Should not have
• Lot of prescriptive words, Clutter

```html
<!DOCTYPE html>
<html lang="en">
<head>
<meta charset="utf-8">
<title>Brightvale Bath Panels &amp; Glass</title>
<link href="https://fonts.googleapis.com/css2?family=Exo+2:ital,wght@0,400;0,600;0,700;0,900;1,900&family=Open+Sans:wght@400;600;700&display=swap" rel="stylesheet">
<style>
:root{
  --navy:#14265c;
  --blue:#0b5bb5;
  --blue-deep:#0a3f8c;
  --ink:#222;
  --muted:#555;
  --pale:#e2ebf6;
  --black:#000;
  --white:#fff;
}
*{margin:0;padding:0;box-sizing:border-box}
html,body{width:1200px;height:4147px;overflow:hidden}
body{position:relative;font-family:"Open Sans",sans-serif;color:var(--ink);background:var(--white)}
.abs{position:absolute}
.head{font-family:"Exo 2",sans-serif}

/* top bar */
.topbar{left:506px;top:0;width:694px;height:39px;background:var(--navy);clip-path:polygon(24px 0,100% 0,100% 100%,0 100%)}
.topbar .call{position:absolute;left:58px;top:10px;color:#fff;font-size:15px;display:flex;align-items:center;gap:8px}
.topbar .mail{position:absolute;left:315px;top:0;width:161px;height:39px;background:var(--blue);color:#fff;font-size:17px;text-align:center;line-height:39px}
.topbar .soc{position:absolute;left:500px;top:12px;display:flex;gap:6px}
.topbar .soc i{display:block;width:15px;height:15px;background:#fff}
.brand{left:86px;top:40px;display:flex;align-items:center;gap:12px;font-family:"Exo 2",sans-serif;font-weight:700;font-size:40px;color:var(--navy)}
.brand i{width:26px;height:26px;background:var(--blue);display:block}
.nav{top:82px;left:0;width:1200px;height:24px;font-size:19px;color:#333}
.nav a{position:absolute;color:inherit;text-decoration:none}
.nav a.on{color:var(--blue)}

/* hero */
.hero{left:0;top:144px;width:1200px;height:553px;background:linear-gradient(100deg,#9ea7ad 0%,#d9dde0 30%,#eef0f1 55%,#c9cdd0 75%,#2b2b2b 100%)}
.hero h1{position:absolute;left:91px;top:190px;font-family:"Exo 2",sans-serif;font-weight:900;font-style:italic;font-size:54px;color:var(--navy);letter-spacing:-.5px}
.hero p{position:absolute;left:94px;top:262px;font-size:29px;font-weight:600;color:#111}
.hero .cta{position:absolute;left:91px;top:312px;width:443px;height:67px;background:var(--blue);color:#fff;font-family:"Exo 2",sans-serif;font-weight:700;font-size:40px;line-height:67px;text-align:center}
.dots{left:1155px;top:368px}
.dots i{display:block;width:12px;height:12px;border-radius:50%;background:#fff;margin-bottom:13px}
.dots i:first-child{background:var(--blue)}

/* welcome */
.welcome-title{left:0;top:805px;width:1200px;text-align:center;font-size:38px;color:#111;font-family:"Exo 2",sans-serif;font-weight:400}
.welcome-title b{color:var(--navy);font-weight:700}
.welcome-text{left:125px;top:880px;width:950px;text-align:center;font-size:14.5px;line-height:29px;color:var(--muted)}
.steps-line{left:190px;top:1165px;width:820px;height:2px;background:var(--navy)}
.step{top:1065px;width:300px;text-align:center}
.step .icon{width:130px;height:110px;margin:0 auto;position:relative}
.step .icon:before{content:"";position:absolute;left:10px;top:30px;width:110px;height:70px;border-radius:55px 55px 0 0;background:#d6e4f3}
.step h3{margin-top:24px;font-family:"Exo 2",sans-serif;font-weight:600;font-size:22px;color:#111}
.step p{margin-top:6px;font-size:14px;line-height:22px;color:var(--muted);padding:0 24px}
.step .chev{margin-top:14px}

/* products */
.prod-band{left:0;top:1416px;width:1200px;height:354px;background:linear-gradient(180deg,#0b4fa8,#0d5cc0)}
.prod-title{left:0;top:1480px;width:1200px;text-align:center;font-family:"Exo 2",sans-serif;font-size:38px;color:#fff}
.prod-title b{font-weight:700}
.card{top:1604px;width:243px;height:332px;background:#fff;box-shadow:0 6px 14px rgba(0,0,0,.18)}
.card .ph{height:276px}
.card span{display:block;text-align:center;line-height:56px;font-size:19px;color:#222}
.tag-line{left:0;top:1990px;width:1200px;text-align:center;font-size:32px;color:#111}
.tag-call{left:0;top:2044px;width:1200px;text-align:center;font-family:"Exo 2",sans-serif;font-weight:700;font-size:34px;color:var(--blue)}

/* testimonials */
.reviews{left:0;top:2157px;width:1200px;height:511px;background:var(--pale)}
.reviews h2{position:absolute;top:100px;width:1200px;text-align:center;font-family:"Exo 2",sans-serif;font-weight:400;font-size:38px;color:#111}
.avatar{position:absolute;left:205px;top:218px;width:188px;height:188px;border-radius:50%;border:4px solid #fff;background:linear-gradient(160deg,#c9ced6,#273a63)}
.quote{position:absolute;left:470px;top:232px;width:545px;font-size:15px;line-height:31px;color:#444}
.quote .who{margin-top:10px;font-size:17px}
.qmark{position:absolute;left:425px;top:228px;font-family:"Exo 2",sans-serif;font-weight:900;font-size:54px;color:var(--blue);line-height:1}
.arrow{position:absolute;top:288px}

/* blog */
.blog-title{left:0;top:2782px;width:1200px;text-align:center;font-family:"Exo 2",sans-serif;font-size:38px;color:#111}
.post{top:2890px;width:312px}
.post .ph{height:171px}
.post .date{margin-top:16px;display:flex;gap:3px}
.post .date span{background:var(--blue);color:#fff;font-size:12px;padding:2px 14px}
.post .date i{display:block;width:34px;height:21px;background:#222}
.post h4{margin-top:10px;font-size:18px;font-weight:700;color:#111}
.post p{margin-top:4px;font-size:14px;line-height:22px;color:var(--muted)}
.post a{display:block;margin-top:4px;font-size:14px;color:var(--blue);text-decoration:none}

/* contact */
.contact-title{left:0;top:3312px;width:1200px;text-align:center;font-family:"Exo 2",sans-serif;font-size:38px;color:#111}
.darkarc{left:0;top:3560px}
.contact-box{left:138px;top:3423px;width:932px;height:387px;background:#fff;border:1px solid #ccc;box-shadow:0 4px 14px rgba(0,0,0,.2)}
.form{position:absolute;left:60px;top:36px;width:326px}
.form h3{font-family:"Exo 2",sans-serif;font-weight:400;font-size:26px;color:#222;margin-bottom:18px}
.form .field{height:40px;border:1px solid #aaa;margin-bottom:10px;font-size:14px;padding:11px 10px;color:#333}
.form .send{margin-top:16px;width:105px;height:32px;border-radius:16px;background:var(--blue);color:#fff;font-weight:700;font-size:18px;text-align:center;line-height:32px;box-shadow:0 3px 0 var(--navy)}
.map{position:absolute;left:445px;top:0;width:486px;height:386px;background:linear-gradient(135deg,#e9ecef,#dcdfe3 50%,#eef0e8)}
.map .search{position:absolute;left:0;top:0;width:486px;height:36px;background:#fff;border-bottom:1px solid #ccc;font-size:12px;color:#555;padding:10px 22px}

/* footer */
.footer{left:0;top:3810px;width:1200px;height:337px;color:#fff}
.fcol{position:absolute;top:57px}
.fcol h5{font-size:16px;font-weight:600;margin-bottom:24px}
.fcol p,.fcol li{font-size:14px;line-height:24px}
.fcol ul{list-style:none}
.fcol li{margin-bottom:8px}
.crow{display:flex;gap:16px;margin-bottom:14px;font-size:14px;line-height:20px}
.frule{left:92px;top:4059px;width:1016px;height:1px;background:#555}
.copy{left:92px;top:4086px;font-size:13px;color:#fff}
.fsoc{left:1022px;top:4084px;display:flex;gap:12px}
.fsoc i{display:block;width:22px;height:22px;background:#fff}
</style>
</head>
<body>

<div class="abs topbar">
  <div class="call">
    <svg width="14" height="14" viewBox="0 0 24 24"><path fill="#fff" d="M6.6 10.8a15 15 0 0 0 6.6 6.6l2.2-2.2a1 1 0 0 1 1-.25 11 11 0 0 0 3.6.57 1 1 0 0 1 1 1V20a1 1 0 0 1-1 1A17 17 0 0 1 3 4a1 1 0 0 1 1-1h3.5a1 1 0 0 1 1 1c0 1.25.2 2.45.57 3.57a1 1 0 0 1-.25 1z"/></svg>
    Call Free: 0800 555 0142
  </div>
  <div class="mail">Email Inquiries</div>
  <div class="soc"><i></i><i></i><i></i><i></i></div>
</div>

<div class="abs brand"><i></i>Brightvale</div>

<nav class="abs nav">
  <a class="on" style="left:462px">Home</a>
  <a style="left:565px">About us</a>
  <a style="left:696px">Services</a>
  <a style="left:821px">Products</a>
  <a style="left:950px">Blog</a>
  <a style="left:1042px">Contact</a>
</nav>

<section class="abs hero" role="img" aria-label="Photo of a bright bathroom with frameless glass shower enclosure">
  <h1>We Love What We Do!</h1>
  <p>Neque porro quisquam est qui dolorem.</p>
  <div class="cta">CALL : 0800 555 0142</div>
</section>
<div class="abs dots"><i></i><i></i><i></i><i></i></div>

<h2 class="abs welcome-title">WELCOME TO <b>BRIGHTVALE BATH PANELS</b></h2>
<p class="abs welcome-text">It is a long established fact that a reader will be distracted by the readable content of a page when looking at its layout. The point of using Lorem Ipsum is that it has a more-or-less normal distribution of letters, as opposed to using 'Content here, content here', making it look like readable English. Many desktop publishing packages and web page editors now use Lorem Ipsum</p>

<div class="abs steps-line"></div>
<svg class="abs" style="left:418px;top:1156px" width="14" height="20" viewBox="0 0 14 20"><path d="M2 2l9 8-9 8" fill="none" stroke="#14265c" stroke-width="2.5"/></svg>
<svg class="abs" style="left:770px;top:1156px" width="14" height="20" viewBox="0 0 14 20"><path d="M2 2l9 8-9 8" fill="none" stroke="#14265c" stroke-width="2.5"/></svg>

<div class="abs step" style="left:95px">
  <div class="icon"><svg style="position:absolute;left:25px;top:5px" width="80" height="90" viewBox="0 0 80 90"><path d="M15 15l50 60M65 15L15 75" stroke="#111" stroke-width="6" fill="none" stroke-linecap="round"/></svg></div>
  <h3>Repair existing shower</h3>
  <p>Lorem Ipsum has been the industry's standard dummy text ever since the 1500s, when an unknown</p>
  <svg class="chev" width="18" height="18" viewBox="0 0 18 18"><path d="M3 3l6 5 6-5M3 10l6 5 6-5" fill="none" stroke="#111" stroke-width="2"/></svg>
</div>
<div class="abs step" style="left:450px">
  <div class="icon"><svg style="position:absolute;left:30px;top:5px" width="70" height="95" viewBox="0 0 70 95"><rect x="10" y="5" width="50" height="85" fill="none" stroke="#111" stroke-width="5"/><path d="M35 5v85" stroke="#111" stroke-width="4"/></svg></div>
  <h3>Tub enclosure</h3>
  <p>Lorem Ipsum has been the industry's standard dummy text ever since the 1500s, when an unknown</p>
  <svg class="chev" width="18" height="18" viewBox="0 0 18 18"><path d="M3 3l6 5 6-5M3 10l6 5 6-5" fill="none" stroke="#111" stroke-width="2"/></svg>
</div>
<div class="abs step" style="left:795px">
  <div class="icon"><svg style="position:absolute;left:35px;top:5px" width="60" height="95" viewBox="0 0 60 95"><path d="M30 5h18v20M15 45a15 15 0 0 1 30 0z" fill="none" stroke="#111" stroke-width="5"/><path d="M20 58v8M30 58v12M40 58v8M25 74v8M35 74v8" stroke="#111" stroke-width="3"/></svg></div>
  <h3>Installation</h3>
  <p>Lorem Ipsum has been the industry's standard dummy text ever since the 1500s, when an unknown</p>
  <svg class="chev" width="18" height="18" viewBox="0 0 18 18"><path d="M3 3l6 5 6-5M3 10l6 5 6-5" fill="none" stroke="#111" stroke-width="2"/></svg>
</div>

<section class="abs prod-band" role="img" aria-label="Blue-toned photo of a glass shower interior"></section>
<h2 class="abs prod-title">OUR <b>PRODUCTS</b></h2>
<div class="abs card" style="left:91px"><div class="ph" role="img" aria-label="Frameless corner shower with clear glass" style="background:linear-gradient(160deg,#d8dcdf,#8f979c)"></div><span>Dolor sit amet</span></div>
<div class="abs card" style="left:351px"><div class="ph" role="img" aria-label="Glass shower with warm stone tiles" style="background:linear-gradient(160deg,#c9a88a,#6d5442)"></div><span>Porro quisquam</span></div>
<div class="abs card" style="left:611px"><div class="ph" role="img" aria-label="Walk-in glass shower with white tiles" style="background:linear-gradient(160deg,#e4e7e9,#9aa2a6)"></div><span>Dolorem ipsum quia</span></div>
<div class="abs card" style="left:871px"><div class="ph" role="img" aria-label="Neo-angle glass shower with beige tiles" style="background:linear-gradient(160deg,#e2c9a7,#9b7a57)"></div><span>Neque porro quisquam</span></div>

<p class="abs tag-line">Neque porro quisquam est qui dolorem.</p>
<p class="abs tag-call">CALL : 0800 555 0142</p>

<section class="abs reviews">
  <h2>Read What Our Customer Say</h2>
  <svg class="arrow" style="left:95px" width="18" height="32" viewBox="0 0 18 32"><path d="M15 2L3 16l12 14" fill="none" stroke="#333" stroke-width="2.5"/></svg>
  <svg class="arrow" style="left:1093px" width="18" height="32" viewBox="0 0 18 32"><path d="M3 2l12 14L3 30" fill="none" stroke="#333" stroke-width="2.5"/></svg>
  <div class="avatar" role="img" aria-label="Customer portrait photo"></div>
  <div class="qmark">&ldquo;</div>
  <div class="quote">
    It is a long established fact that a reader will be distracted by the readable content of a page when looking at its layout. The point of using Lorem Ipsum is that it has a more-or-less normal distribution of letters, as opposed to using 'Content here, content here', making it look like readable English.
    <div class="who">- Neque porro quisquam</div>
  </div>
</section>

<h2 class="abs blog-title">Latest Blog</h2>
<article class="abs post" style="left:97px">
  <div class="ph" role="img" aria-label="Person cleaning a glass shower door" style="background:linear-gradient(135deg,#f1e3b8,#d8a9a0)"></div>
  <div class="date"><span>Dec 03</span><i></i></div>
  <h4>Neque porro quisquam dolorem</h4>
  <p>It has survived not only five centuries, but also the leap into electronic typesetting.</p>
  <a>Read More &raquo;</a>
</article>
<article class="abs post" style="left:445px">
  <div class="ph" role="img" aria-label="Technician repairing a shower fitting" style="background:linear-gradient(135deg,#eceff2,#2d3f6d)"></div>
  <div class="date"><span>Dec 03</span><i></i></div>
  <h4>Porro quisquam est qui</h4>
  <p>It has survived not only five centuries, but also the leap into electronic typesetting.</p>
  <a>Read More &raquo;</a>
</article>
<article class="abs post" style="left:796px">
  <div class="ph" role="img" aria-label="Installer fitting a glass shower panel" style="background:linear-gradient(135deg,#b7b3ab,#e8e6e1)"></div>
  <div class="date"><span>Dec 03</span><i></i></div>
  <h4>Dolorem ipsum quia dolor</h4>
  <p>It has survived not only five centuries, but also the leap into electronic typesetting.</p>
  <a>Read More &raquo;</a>
</article>

<h2 class="abs contact-title">Contact Us</h2>
<svg class="abs darkarc" width="1200" height="587" viewBox="0 0 1200 587"><path d="M0 10 Q600 330 1200 10 L1200 587 L0 587 Z" fill="#000"/></svg>

<section class="abs contact-box">
  <div class="form">
    <h3>Appointment</h3>
    <div class="field">Name</div>
    <div class="field">Phone number</div>
    <div class="field">Email address</div>
    <div class="field">Message</div>
    <div class="send">SEND</div>
  </div>
  <div class="map" role="img" aria-label="Street map showing the business location">
    <div class="search">Find your location
      <svg style="position:absolute;right:12px;top:10px" width="16" height="16" viewBox="0 0 16 16"><circle cx="6.5" cy="6.5" r="4.5" fill="none" stroke="#333" stroke-width="2"/><path d="M10 10l4 4" stroke="#333" stroke-width="2"/></svg>
    </div>
  </div>
</section>

<footer class="abs footer">
  <div class="fcol" style="left:140px;width:300px">
    <h5>ABOUT BRIGHTVALE BATH PANELS</h5>
    <p>The point of using Lorem Ipsum is that it has a more-or-less normal distribution of letters, as opposed to using 'Content here, content here', making it look like readable English.</p>
  </div>
  <div class="fcol" style="left:520px">
    <h5>LINK</h5>
    <ul><li>Home</li><li>About Us</li><li>Services</li></ul>
  </div>
  <div class="fcol" style="left:636px">
    <h5>SERVICES</h5>
    <ul><li>Repair existing shower</li><li>Tub enclosure</li><li>Installation</li></ul>
  </div>
  <div class="fcol" style="left:852px;width:260px">
    <h5>CONTACT US</h5>
    <div class="crow"><svg width="16" height="20" viewBox="0 0 16 20"><path d="M8 1a6 6 0 0 0-6 6c0 5 6 12 6 12s6-7 6-12a6 6 0 0 0-6-6z" fill="#fff"/><circle cx="8" cy="7" r="2" fill="#000"/></svg><span>12 Linden Row,<br>Westbrook 40210</span></div>
    <div class="crow"><svg width="16" height="16" viewBox="0 0 24 24"><path fill="#fff" d="M6.6 10.8a15 15 0 0 0 6.6 6.6l2.2-2.2a1 1 0 0 1 1-.25 11 11 0 0 0 3.6.57 1 1 0 0 1 1 1V20a1 1 0 0 1-1 1A17 17 0 0 1 3 4a1 1 0 0 1 1-1h3.5a1 1 0 0 1 1 1c0 1.25.2 2.45.57 3.57a1 1 0 0 1-.25 1z"/></svg><span>0800 555 0142</span></div>
    <div class="crow"><svg width="16" height="14" viewBox="0 0 16 14"><rect x="1" y="2" width="14" height="10" fill="none" stroke="#fff" stroke-width="1.6"/><path d="M1 2l7 6 7-6" fill="none" stroke="#fff" stroke-width="1.6"/></svg><span>info@brightvalebaths-demo.com</span></div>
  </div>
</footer>
<div class="abs frule"></div>
<p class="abs copy">Copyright &copy; 2019. All Rights Reserved</p>
<div class="abs fsoc"><i></i><i></i><i></i></div>

</body>
</html>
```